Award-winnning Estate Agent needs a premium version of their 'For Sale' board design

We need a premium option for our 'For Sale' board design. We have a standard board that is attached to this brief, but were are looking to have a premium design version that we will use when selling exclusive properties. Our company name is Harbour Lane Estates and the name for this is exclusive selection is: 'The Harbour Collection'. The design needs to work with our current brand, but have a distinctive PREMIUM feel to it. I have uploaded the barnd guidelines and also some of the exisisting logo variations. We do NOT need a new logo but feel free to play around with colours, fonts, sizes etc. for the sign.

Target Market(s)

Property buyers & house hunters

Industry/Entity Type

Real Estate - Residential Property

Font styles to use
Sans Serif

Requirements
Must have
• A premium fee, must be square design, must be easy to read when driving past the sign
Nice to have
• I'm open ot ideas

```html
<!DOCTYPE html>
<html lang="en">
<head>
<meta charset="utf-8">
<title>Harbour Lane Estates – The Harbour Collection For Sale Board</title>
<link rel="stylesheet" href="https://fonts.googleapis.com/css2?family=Arimo:wght@400&family=Libre+Baskerville:wght@700&display=swap">
<style>
  :root {
    --navy: #011638;
    --gold: #b89b52;
    --white: #ffffff;
    --backdrop: #e9e9e6;
    --serif: "Libre Baskerville", Georgia, serif;
    --sans: "Arimo", Arial, sans-serif;
  }
  * { margin: 0; padding: 0; box-sizing: border-box; }
  html, body {
    width: 720px;
    height: 1200px;
    overflow: hidden;
    background: var(--backdrop);
  }
  .board {
    position: absolute;
    top: 240px;
    left: 0;
    width: 720px;
    height: 720px;
    background: var(--navy);
    overflow: hidden;
  }
  .board__frame {
    position: absolute;
    left: 20px;
    top: 18px;
    width: 680px;
    height: 680px;
    border: 4px solid var(--gold);
  }
  .board__band {
    position: absolute;
    left: 0;
    top: 67px;
    width: 720px;
    height: 161px;
    background: var(--gold);
    display: flex;
    align-items: center;
    justify-content: center;
  }
  .board__headline {
    font-family: var(--serif);
    font-weight: 700;
    font-size: 104px;
    line-height: 1;
    color: var(--white);
    letter-spacing: 1px;
    padding-top: 8px;
  }
  .board__collection {
    position: absolute;
    left: 0;
    width: 720px;
    top: 428px;
    text-align: center;
    font-family: var(--sans);
    font-weight: 400;
    font-size: 46px;
    line-height: 1;
    color: var(--white);
    letter-spacing: -0.5px;
  }
  .board__rule {
    position: absolute;
    left: 243px;
    top: 512px;
    width: 234px;
    height: 3px;
    background: var(--gold);
  }
  .board__phone {
    position: absolute;
    left: 0;
    width: 720px;
    top: 532px;
    text-align: center;
    font-family: var(--serif);
    font-weight: 700;
    font-size: 72px;
    line-height: 1;
    color: var(--white);
    letter-spacing: 6px;
    word-spacing: 14px;
  }
  .board__web {
    position: absolute;
    left: 0;
    width: 720px;
    top: 620px;
    text-align: center;
    font-family: var(--sans);
    font-weight: 400;
    font-size: 34px;
    line-height: 1;
    color: var(--gold);
  }
</style>
</head>
<body>
  <main class="board">
    <div class="board__frame"></div>
    <div class="board__band">
      <h1 class="board__headline">FOR SALE</h1>
    </div>
    <p class="board__collection">The Harbour Collection</p>
    <div class="board__rule"></div>
    <p class="board__phone">01632 960481</p>
    <p class="board__web">www.harbourlaneestates.co.uk</p>
  </main>
</body>
</html>
```